Kiswa Design

We need a flyer design for a product that we are a selling, a sacred Islamic cloth called a Kiswah, which is draped around the holy Kaaba in mecca every year.

The details we would like on the flyer are as follows:

Rare Kiswah of the holy Kaaba for sale (fitted in 1977 and 1982 vintage). For sale:

1) whole piece 15 meters x 2.60 meters : £60,000
2) 8 meters x 2.60 meters : £31,200
3) 4 meters x 2.60 meters : £15,600
4) 1 meter : £1500

(insert a high quality picture of holy Kaaba here, then underneath the picture, write the following:) "The Kaaba is covered by an expensive black cloth which is known as 'Kiswah' which is produced and changed every year"

(insert picture of our product here,i.e. use the document named MAIN IMAGE then underneath this picture write the following:) "Silk lampas weave Kiswah, woven silk on a black satin ground with Quranic calligraphy, the zig-zag bands of inscription alternate with the Shahadah and the inscription, 'God, exalted be His Glory!"

insert another picture of kiswah which i provided anywhere you like

(somewhere on flyer write the following) please note a percentage of sales will go towards Sadaqah for our Muslim brothers and sisters in need around the world

(somewhere on flyer write the following) Hallorand's international auction house authenticity document also available to prove the Kiswah is genuine.

100% genuine

contact us today! deals this good don't last forever.

email: relicoffer@tarnwickmail.com

Please use the images that I have attached on the flyer accordingly. Also feel free to be as creative as possible I want it to attract a lot of attention but also look professional so you may add some things to improve the look of the flyer.

note: the product being sold is on the pictures I've provided, in particular, i want file 2 "main image" in a large size on the flyer!

thank you! and happy holidays

Muslims and Islamic collectors

House

• the dimensions of the flyer is :
• A5 horizontal or vertical
• (210 x 148 mm)
• must have colors! up to you what colors to choose!

```html
<!DOCTYPE html>
<html lang="en">
<head>
<meta charset="utf-8">
<title>Rare Kiswah of the Holy Kaa'ba – For Sale</title>
<link href="https://fonts.googleapis.com/css2?family=Anton&family=Archivo+Black&family=Roboto:wght@900&family=Roboto+Condensed:ital,wght@0,700;1,700&display=swap" rel="stylesheet">
<style>
  :root {
    --red: #e8161b;
    --red-text: #e0181c;
    --green: #2b9a2c;
    --green-deep: #0e8a12;
    --yellow: #e9e23a;
    --pale: #f1f0e6;
    --black: #0a0a0a;
    --white: #ffffff;
  }
  * { margin: 0; padding: 0; box-sizing: border-box; }
  html, body { width: 846px; height: 1200px; overflow: hidden; }
  body { background: var(--white); }
  .flyer {
    position: relative; width: 846px; height: 1200px; overflow: hidden;
    background: linear-gradient(100deg, var(--pale) 0%, #eeedcf 40%, #eae56b 75%, var(--yellow) 100%);
    font-family: "Roboto Condensed", "Arial Narrow", sans-serif;
    color: var(--black);
  }
  .top-band {
    position: absolute; left: 0; top: 0; width: 846px; height: 104px;
    background: var(--red); display: flex; align-items: center; justify-content: center;
  }
  .top-band h1 {
    font-family: "Anton", "Impact", sans-serif; font-weight: 400;
    font-size: 92px; letter-spacing: 9px; line-height: 1; color: var(--black);
  }
  .ornament { position: absolute; border-radius: 50%; opacity: .35; }
  .ornament.left { left: 40px; top: 190px; width: 240px; height: 110px;
    background: radial-gradient(ellipse, #d9c27a 0%, rgba(217,194,122,0) 70%); }
  .ornament.right { left: 660px; top: 200px; width: 170px; height: 150px;
    background: radial-gradient(ellipse, #d7bd5e 0%, rgba(215,189,94,0) 70%); }
  .title {
    position: absolute; left: 0; width: 846px; top: 118px; text-align: center;
    font-family: "Roboto", Arial, sans-serif; font-weight: 900;
    font-size: 62px; line-height: 70px; color: var(--green);
  }
  .vintage {
    position: absolute; left: 0; width: 846px; top: 272px; text-align: center;
    font-style: italic; font-weight: 700; font-size: 31px; font-family: "Roboto", Arial, sans-serif;
  }
  .left-panel {
    position: absolute; left: 0; top: 322px; width: 416px; height: 843px;
    background: linear-gradient(150deg, var(--green-deep) 0%, #5cb85a 12%, #f5f7ef 42%, #ffffff 55%, #cfe8c9 78%, var(--green-deep) 100%);
    border-top: 4px solid var(--green-deep); border-right: 12px solid var(--green-deep);
  }
  .photo { position: absolute; }
  .photo.kaaba { left: 20px; top: 22px; width: 380px; height: 229px;
    background: linear-gradient(180deg, #bfc4c8 0%, #3a3c3c 35%, #1a1a1a 60%, #7d7a72 100%); }
  .photo.cloth-main { left: 20px; top: 362px; width: 230px; height: 270px;
    background: linear-gradient(160deg, #5a5a5c 0%, #2c2c2e 55%, #1d1d1f 100%); }
  .photo.cloth-folded { left: 228px; top: 382px; width: 164px; height: 226px;
    background: linear-gradient(170deg, #f2f2f2 0%, #2b2b2b 30%, #141414 100%); border: 3px solid var(--white); }
  .caption { position: absolute; left: 20px; width: 372px; font-weight: 700; font-size: 17.5px; line-height: 22px; }
  .caption.first { top: 258px; }
  .caption.second { top: 642px; }
  .genuine {
    position: absolute; left: 418px; width: 428px; text-align: center;
    font-family: "Anton", "Impact", sans-serif; color: var(--red-text);
    text-shadow: 3px 4px 4px rgba(0,0,0,.35);
  }
  .genuine.pct { top: 322px; font-size: 100px; line-height: 120px; }
  .genuine.word { top: 428px; font-size: 96px; line-height: 116px; }
  .prices { position: absolute; left: 432px; top: 550px; }
  .prices h2 { font-family: "Archivo Black", "Arial Black", sans-serif; font-weight: 400; font-size: 27px; line-height: 34px; letter-spacing: .5px; }
  .prices p { font-weight: 700; font-size: 24px; line-height: 30px; }
  .prices .gap-s { margin-top: 6px; }
  .prices .gap-m { margin-top: 8px; }
  .prices .gap-l { margin-top: 20px; }
  .auth-box {
    position: absolute; left: 418px; top: 843px; width: 428px; height: 85px;
    background: var(--red); color: var(--white); text-align: center;
    font-weight: 700; font-size: 18.5px; line-height: 21px; padding-top: 9px;
  }
  .deals {
    position: absolute; left: 418px; width: 428px; top: 936px; text-align: center;
    font-family: "Archivo Black", "Arial Black", sans-serif; color: var(--red-text);
    font-size: 31px; line-height: 37px;
  }
  .contact {
    position: absolute; left: 418px; width: 428px; top: 1020px; text-align: center;
    font-family: "Archivo Black", "Arial Black", sans-serif; font-style: italic;
    font-size: 40px; line-height: 56px;
  }
  .email-band {
    position: absolute; left: 418px; top: 1084px; width: 428px; height: 78px;
    background: var(--red); color: var(--white); display: flex; align-items: center; justify-content: center;
    font-weight: 700; font-size: 31px;
  }
  .footer {
    position: absolute; left: 0; top: 1165px; width: 846px; height: 35px;
    background: #fbfbf3; text-align: center; font-style: italic; font-weight: 700; font-size: 15px; line-height: 35px;
  }
</style>
</head>
<body>
<div class="flyer">
  <header class="top-band"><h1>FOR SALE</h1></header>

  <div class="ornament left" role="img" aria-label="Faint golden Arabic calligraphy"></div>
  <div class="ornament right" role="img" aria-label="Faint golden Arabic calligraphy"></div>

  <div class="title">Rare Kiswah of the<br>Holy Kaa’ba</div>
  <div class="vintage">Fitted in 1977 and 1982 Vintage</div>

  <section class="left-panel">
    <div class="photo kaaba" role="img" aria-label="Photograph of the Kaaba draped in its black kiswah, surrounded by pilgrims"></div>
    <p class="caption first">The Kaa’ba is covered by an expensive black cloth known as ‘kiswah which is produced and changed every year.</p>
    <div class="photo cloth-main" role="img" aria-label="Close-up of black kiswah silk with woven calligraphy"></div>
    <div class="photo cloth-folded" role="img" aria-label="Folded piece of black kiswah cloth"></div>
    <p class="caption second">Silk lampas weave Kiswah, woven silk on a blacksatin ground with Quranic calligraphy, the zig-zag bands of inscription alternate with the Shahadah and the inscription, 'God, exalted be His Glory!"</p>
  </section>

  <div class="genuine pct">100%</div>
  <div class="genuine word">GENUINE</div>

  <section class="prices">
    <h2>WHOLE PIECE</h2>
    <p class="gap-s">15 meters x 2.60 meters:&nbsp; £60,000</p>
    <h2 class="gap-m">RETAIL PIECES</h2>
    <p class="gap-s">8 meters x 2.60 meters: £31,200</p>
    <p class="gap-l">4 meters x 2.60 meters: £15,600</p>
    <p class="gap-l">1 meter: £1,500</p>
  </section>

  <div class="auth-box">Hallorand's international auction house<br>authenticity document also available<br>to prove the Kiswa is genuine.</div>

  <div class="deals">Deals this good<br>don't last forever!</div>
  <div class="contact">Contact us today!</div>
  <div class="email-band">relicoffer@tarnwickmail.com</div>

  <footer class="footer">A percentage of sales will go towards Sadaqah for our Muslim brothers and sisters in need around the world.</footer>
</div>
</body>
</html>
```